Cosmetic injections clinic needs a fresh looking business card

We need a business card using the supplied logo and color scheme to attract future clients to our clinic. It should be modern and fresh, eye catching and not too busy. Simple and to the point is best. I would like two sided designs with the front indicating address and contact information, and the back in full color with white logo and descriptive information also provided.
Target Market(s)
Clients looking for non surgical beauty enhancements.
Contact Information for Business Card
MeloraSkin
14, 618 Birchmont Way
Larkfield, Ontario
K2P 7W3
Phone: 587-412-6630
Email: info@meloraskin.com
Requirements
Must have
- -Logo supplied with the name and address of the clinic
- -Back of card in full color with white logo with A small line of text indicating both of the following: Anti aging consultants and cosmetic injectables
- Located inside the Voyager Wellness Group

```html
<!DOCTYPE html>
<html lang="en">
<head>
<meta charset="utf-8">
<title>MeloraSkin Business Card</title>
<link rel="stylesheet" href="https://fonts.googleapis.com/css2?family=Quicksand:wght@400;500;600;700&display=swap">
<style>
  :root {
    --teal: #2bbdbb;
    --plum: #5a2e8c;
    --ink: #3a3a3a;
    --rule: #555555;
    --paper: #f7f7f7;
    --backdrop: #e9e6e1;
    --white: #ffffff;
  }
  * { box-sizing: border-box; margin: 0; padding: 0; }
  html, body {
    width: 1200px; height: 1050px; overflow: hidden;
    background: var(--backdrop);
    font-family: "Quicksand", sans-serif;
  }
  .canvas {
    width: 1200px; height: 1050px;
    display: flex; flex-direction: column; align-items: center;
    padding-top: 50px; gap: 70px;
  }
  .card {
    flex: none;
    width: 760px; height: 435px;
    border-radius: 4px;
    box-shadow: 0 6px 18px rgba(0,0,0,0.14);
    position: relative;
    overflow: hidden;
  }
  /* Front */
  .card-front {
    background: var(--paper);
    display: flex; align-items: center;
  }
  .front-brand {
    width: 330px;
    display: flex; align-items: center; justify-content: center; gap: 12px;
  }
  .brand-dot {
    flex: none;
    width: 20px; height: 20px; border-radius: 50%;
    background: var(--plum);
  }
  .brand-name {
    font-weight: 700; font-size: 40px; color: var(--plum);
    letter-spacing: 0.5px; white-space: nowrap;
  }
  .front-divider {
    flex: none;
    width: 2px; height: 280px; background: var(--rule);
  }
  .front-contact {
    padding-left: 42px;
  }
  .contact-name {
    font-size: 34px; font-weight: 600; color: var(--teal); line-height: 1;
  }
  .contact-tagline {
    font-size: 15px; font-weight: 500; color: var(--ink);
    letter-spacing: 1px; margin-top: 6px; margin-bottom: 40px;
  }
  .contact-list { list-style: none; }
  .contact-item {
    display: flex; align-items: flex-start; gap: 13px;
    font-size: 18px; font-weight: 500; color: var(--ink);
    line-height: 1.3; margin-bottom: 20px;
  }
  .contact-icon {
    flex: none; width: 20px; height: 20px; margin-top: 2px;
    background: var(--teal); border-radius: 3px;
    display: flex; align-items: center; justify-content: center;
  }
  /* Back */
  .card-back {
    background: var(--teal);
    display: flex; flex-direction: column; align-items: center;
    color: var(--white);
    padding-top: 118px;
  }
  .back-brand {
    display: flex; align-items: center; gap: 14px;
  }
  .back-brand .brand-dot { background: var(--white); width: 24px; height: 24px; }
  .back-brand .brand-name { color: var(--white); font-size: 58px; }
  .back-rule {
    width: 42px; height: 2px; background: var(--white);
    margin: 38px 0 26px;
  }
  .back-line {
    font-size: 20px; font-weight: 500; line-height: 1.75;
  }
</style>
</head>
<body>
<main class="canvas">
  <section class="card card-front" aria-label="Business card front">
    <div class="front-brand">
      <span class="brand-dot"></span>
      <span class="brand-name">MeloraSkin</span>
    </div>
    <div class="front-divider"></div>
    <div class="front-contact">
      <h1 class="contact-name">MeloraSkin</h1>
      <p class="contact-tagline">COSMETIC CLINIC</p>
      <ul class="contact-list">
        <li class="contact-item">
          <span class="contact-icon">
            <svg width="13" height="13" viewBox="0 0 24 24"><path fill="#fff" d="M6.6 10.8a15.1 15.1 0 0 0 6.6 6.6l2.2-2.2c.3-.3.7-.4 1-.2 1.1.4 2.3.6 3.6.6.6 0 1 .4 1 1V20c0 .6-.4 1-1 1C10.6 21 3 13.4 3 4c0-.6.4-1 1-1h3.5c.6 0 1 .4 1 1 0 1.3.2 2.5.6 3.6.1.3 0 .7-.2 1z"/></svg>
          </span>
          <span>587.412.6630</span>
        </li>
        <li class="contact-item">
          <span class="contact-icon">
            <svg width="13" height="13" viewBox="0 0 24 24"><rect x="2" y="5" width="20" height="14" rx="1.5" fill="#fff"/><path d="M3 6l9 7 9-7" stroke="#2bbdbb" stroke-width="2" fill="none"/></svg>
          </span>
          <span>info@meloraskin.com</span>
        </li>
        <li class="contact-item">
          <span class="contact-icon">
            <svg width="13" height="13" viewBox="0 0 24 24"><path fill="#fff" d="M12 2a7 7 0 0 0-7 7c0 5.2 7 13 7 13s7-7.8 7-13a7 7 0 0 0-7-7zm0 9.5A2.5 2.5 0 1 1 12 6.5a2.5 2.5 0 0 1 0 5z"/></svg>
          </span>
          <span>14, 618 Birchmont Way<br>Larkfield, Ontario<br>K2P 7W3</span>
        </li>
      </ul>
    </div>
  </section>

  <section class="card card-back" aria-label="Business card back">
    <div class="back-brand">
      <span class="brand-dot"></span>
      <span class="brand-name">MeloraSkin</span>
    </div>
    <div class="back-rule"></div>
    <p class="back-line">Anti aging consultants and cosmetic injectables</p>
    <p class="back-line">Located inside the Voyager Wellness Group</p>
  </section>
</main>
</body>
</html>
```